Broschüren-Design für Versicherungsagenten
Zielgruppe
Ich bin mit KL-Vorsorge als unabhängiger Versicherungsagent Selbstständig. (www.kl-vorsorge.de)
Ich habe mich auf die Absicherung von biometrischen Risiken spezialisiert - die auch in der Broschüre Thematisiert werden sollen. Das Oberthema der Broschüre ist 'biometrische Risiken'. Dies soll dann auf die Themen: Arbeitskraft, Langlebigkeit und Pflege heruntergebrochen werden.
Zielgruppe sind vor allem junge Menschen, die gerade erst eine Ausbildung gestartet oder ihr Studium beendet haben.
Aufgabenstellung
Das Design sollte die drei Hauptbereiche: Arbeitskraft, Langlebigkeit und Pflege, leicht verständlich dem Kunden veranschaulichen. Texte, Informationen und Grafiken (in der Reihenfolge, so wie ich mir das vorstelle) sind als Datei beigefügt.
Das ganze soll im DIN A4 Format gedruckt werden, wobei ich auf einen Hochwertigen Druck inklusive Druckveredelung hohen Wert lege.

```html
<!DOCTYPE html>
<html lang="de">
<head>
<meta charset="utf-8">
<title>Broschüre – Biometrische Risiken</title>
<link rel="stylesheet" href="https://fonts.googleapis.com/css2?family=Montserrat:wght@400;600&family=Share+Tech+Mono&display=swap">
<style>
  :root {
    --bg: #ececec;
    --page: #f4f4f4;
    --page-shade: #e6e6e6;
    --ink: #2b2b2b;
    --ink-soft: #555555;
    --accent: #d9a04e;
    --photo-dark: #4a4a4a;
    --photo-light: #a9a9a9;
  }
  * { box-sizing: border-box; margin: 0; padding: 0; }
  html, body { width: 1200px; height: 857px; overflow: hidden; }
  body {
    background: var(--bg);
    font-family: "Montserrat", sans-serif;
    color: var(--ink);
    display: flex;
    align-items: center;
    justify-content: center;
  }
  .spread {
    display: flex;
    width: 1120px;
    height: 400px;
    box-shadow: 0 14px 40px rgba(0,0,0,0.18);
  }
  .page {
    position: relative;
    width: 560px;
    height: 400px;
    background: var(--page);
    overflow: hidden;
  }
  .page--left { background: linear-gradient(90deg, var(--page) 85%, var(--page-shade)); }
  .page--right { background: linear-gradient(90deg, var(--page-shade), var(--page) 15%); }

  .heading {
    font-family: "Share Tech Mono", monospace;
    font-weight: 400;
    letter-spacing: 0.22em;
    text-transform: uppercase;
    color: var(--ink);
  }
  .chevrons {
    color: var(--accent);
    letter-spacing: 0.05em;
    margin-left: 14px;
  }

  .about {
    position: absolute;
    left: 32px;
    top: 58px;
    width: 240px;
  }
  .about .heading { font-size: 22px; margin-bottom: 28px; }
  .about p {
    font-size: 9.5px;
    line-height: 1.45;
    color: var(--ink-soft);
    margin-bottom: 12px;
    text-align: left;
  }
  .about strong { font-weight: 600; color: var(--ink); }

  .photo {
    position: absolute;
    right: 0;
    top: 0;
    width: 270px;
    height: 400px;
    background: linear-gradient(160deg, var(--photo-light), var(--photo-dark) 70%);
  }

  .intro {
    position: absolute;
    left: 44px;
    top: 48px;
    width: 300px;
    font-size: 8px;
    line-height: 1.6;
    color: var(--ink-soft);
  }
  .topic-title {
    position: absolute;
    left: 44px;
    top: 130px;
    font-size: 20px;
    letter-spacing: 0.18em;
    white-space: nowrap;
  }
  .topic-text {
    position: absolute;
    left: 44px;
    top: 170px;
    width: 300px;
    font-size: 8px;
    line-height: 1.6;
    color: var(--ink-soft);
  }
  .section {
    position: absolute;
    left: 0;
    bottom: 42px;
    display: flex;
    align-items: center;
  }
  .section__dot {
    width: 44px;
    height: 44px;
    border-radius: 50%;
    background: var(--accent);
    margin-left: -22px;
    margin-right: 16px;
    flex: none;
  }
  .section .heading { font-size: 18px; }
  .section__question {
    font-size: 8.5px;
    color: var(--ink-soft);
    margin-top: 4px;
    letter-spacing: 0.02em;
  }
</style>
</head>
<body>
  <main class="spread">
    <section class="page page--left">
      <div class="about">
        <h2 class="heading">Über uns<span class="chevrons">&gt;&gt;&gt;</span></h2>
        <p>Die meisten Menschen sind sich der herrschenden Probleme der fehlenden Absicherung der Arbeitskraft, der Altersarmut und des Pflegenotstands sehr wohl bewusst. Allerdings mangelt es noch an Handlungen.</p>
        <p>Dies liegt sehr oft daran, dass der Ansprechpartner/Problemlöser in diesem Bereich fehlt. Genau da stellen wir uns auf!</p>
        <p><strong>Wir stehen für:</strong><br>TOP Bedingungen<br>den besten Versicherungsschutz</p>
        <p>Es ist Aufgabe des Vermittlers, Angaben in den Bedingungen &amp; den Tarifen zu überprüfen und zu gewichten.</p>
      </div>
      <div class="photo" role="img" aria-label="Schwarz-Weiß-Foto: Gesprächssituation am Tisch mit aufgeklapptem Laptop"></div>
    </section>

    <section class="page page--right">
      <p class="intro">Wer früh vorsorgt, bleibt flexibel – auch wenn das Leben schneller wird als geplant. Genau das ist heute ein Gebot der Vernunft.</p>
      <h1 class="heading topic-title">Biometrischen Risikoabsicherung</h1>
      <p class="topic-text">Biometrische Risiken werden die Risiken genannt, die unmittelbar mit Ihrem Leben verknüpft sind.</p>
      <div class="section">
        <span class="section__dot"></span>
        <div>
          <h2 class="heading">Pflege<span class="chevrons">&gt;&gt;&gt;</span></h2>
          <p class="section__question">Können Sie Ihr tägliches Leben noch selbst bewältigen?</p>
        </div>
      </div>
    </section>
  </main>
</body>
</html>
```